Ashby Meadows Thank-You Tag

Looking for a file that incorporates current branding/colors and says:

"Thanks for Swimming with Us!"
Ashby Meadows Otters

Samples of other pieces we've done recently are attached.

Will be printed on cardstock that is
Width: 3.5 inches
Height: 2.5 inches

```html
<!DOCTYPE html>
<html lang="en">
<head>
<meta charset="utf-8">
<title>Ashby Meadows Thank-You Tag</title>
<link rel="stylesheet" href="https://fonts.googleapis.com/css2?family=Anton&family=Poppins:wght@600;700;800&display=swap">
<style>
  :root {
    --navy: #1c4087;
    --navy-soft: #2b4f95;
    --pink: #ef4f9b;
    --sky: #8fb6e0;
    --white: #ffffff;
    --pattern: #5f7fbf;
  }
  * { margin: 0; padding: 0; box-sizing: border-box; }
  html, body { width: 1200px; height: 858px; overflow: hidden; background: var(--white); }
  .stage { position: relative; width: 1200px; height: 858px; overflow: hidden; font-family: "Poppins", sans-serif; }
  .backdrop { position: absolute; inset: 0; }

  /* Each panel is a 2.5 x 3.5 in tag face */
  .card { position: absolute; top: 102px; width: 467px; height: 654px; overflow: hidden; }

  /* Front: year card */
  .card--front { left: 111px; background: var(--navy); }
  .front__texture { position: absolute; inset: 0; background: linear-gradient(160deg, var(--navy-soft), var(--navy)); }
  .year { position: absolute; font-family: "Poppins", sans-serif; font-weight: 700; font-size: 170px; line-height: 1; }
  .year--a { left: 236px; top: 349px; color: var(--pink); }
  .year--b { left: 272px; top: 497px; color: var(--white); }
  .year--c { left: 352px; top: 497px; color: var(--pink); }
  .badge {
    position: absolute; left: 368px; top: 378px; width: 88px; height: 88px;
    border-radius: 50%; background: var(--white);
    display: flex; align-items: center; justify-content: center; text-align: center;
    color: var(--navy); font-weight: 700; font-size: 11px; line-height: 1.2;
    box-shadow: inset 0 0 0 5px var(--white), inset 0 0 0 7px var(--navy);
  }

  /* Back: thank-you message */
  .card--back { left: 623px; background: var(--navy); }
  .back__wave { position: absolute; left: 0; top: 0; }
  .splash {
    position: absolute; left: 262px; top: 0; width: 180px; height: 90px;
    background: var(--navy); border-radius: 0 0 50px 80px;
  }
  .headline { position: absolute; left: 0; width: 100%; text-align: center; line-height: 1; white-space: nowrap; }
  .headline--thanks { top: 103px; font-family: "Anton", sans-serif; font-size: 100px; letter-spacing: 12px; text-indent: 12px; color: var(--navy); }
  .headline--for { top: 226px; font-weight: 800; font-size: 52px; color: var(--white); }
  .headline--swimming { top: 275px; font-weight: 800; font-size: 72px; color: var(--pink); }
  .headline--with { top: 339px; font-weight: 800; font-size: 80px; color: var(--white); }
  .headline--with .accent { color: var(--sky); }
  .dash { position: absolute; top: 240px; }
  .dash--left { left: 86px; }
  .dash--right { left: 330px; }
  .team-name {
    position: absolute; left: 0; top: 478px; width: 100%; text-align: center;
    color: var(--white); font-weight: 800; font-size: 30px; line-height: 1.1;
  }
  .border-strip { position: absolute; left: 0; bottom: 0; width: 100%; height: 31px; background: var(--pattern); }
</style>
</head>
<body>
<main class="stage">
  <svg class="backdrop" width="1200" height="858" viewBox="0 0 1200 858">
    <polygon points="0,0 1200,0 1200,858 672,858" fill="var(--sky)"/>
  </svg>

  <section class="card card--front">
    <div class="front__texture" role="img" aria-label="Repeating club emblem pattern in soft blue"></div>
    <span class="year year--a">2</span>
    <div class="badge">Ashby<br>Meadows</div>
    <span class="year year--b">2</span>
    <span class="year year--c">6</span>
  </section>

  <section class="card card--back">
    <svg class="back__wave" width="467" height="654" viewBox="0 0 467 654">
      <path d="M0,0 H467 V190 C390,178 310,196 230,196 C150,196 70,198 0,206 Z" fill="var(--white)"/>
    </svg>
    <div class="splash" role="img" aria-label="Water splash illustration"></div>
    <h1 class="headline headline--thanks">THANKS</h1>
    <svg class="dash dash--left" width="46" height="16" viewBox="0 0 46 16"><path d="M3,12 Q23,0 43,6" stroke="var(--pink)" stroke-width="6" fill="none" stroke-linecap="round"/></svg>
    <svg class="dash dash--right" width="46" height="16" viewBox="0 0 46 16"><path d="M3,6 Q23,0 43,12" stroke="var(--pink)" stroke-width="6" fill="none" stroke-linecap="round"/></svg>
    <p class="headline headline--for">FOR</p>
    <p class="headline headline--swimming">SWIMMING</p>
    <p class="headline headline--with">WITH <span class="accent">US!</span></p>
    <p class="team-name">Ashby Meadows<br>Otters</p>
    <div class="border-strip" role="img" aria-label="Decorative water splash border pattern"></div>
  </section>
</main>
</body>
</html>
```